Commercial Office Fitout company needs a simple website

We need a website for our company Harbourline Fitouts (QLD) Pty Ltd. We are in the construction industry and we specialise in commercial office fitouts (partitions/glass/doors). Our company colours are black and silver. Please use our logo attached.
We only need an "about us" section, a "portfolio" section where we display some pictures of our work, and a "contact us" section. We would like our website to be simple, effective, professional and modern.

Industry/Entity Type

Construction

Number of Pages Required

1 page

```html
<!DOCTYPE html>
<html lang="en">
<head>
<meta charset="utf-8">
<title>Harbourline Fitouts</title>
<link href="https://fonts.googleapis.com/css2?family=Roboto:wght@300;400;500;700&display=swap" rel="stylesheet">
<style>
:root{
  --ink:#1d1d1f;
  --dark:#222326;
  --darker:#18191b;
  --silver:#b9bcc1;
  --mid:#7b7e84;
  --light:#f1f1f2;
  --line:#d5d6d8;
  --white:#ffffff;
  --accent:#444;
}
*{box-sizing:border-box;margin:0;padding:0}
html,body{width:700px;height:1200px;overflow:hidden;background:var(--white);font-family:'Roboto',Arial,sans-serif;color:var(--ink)}
.page{position:relative;width:700px;height:1200px;overflow:hidden}

/* top bar */
.topbar{position:absolute;top:0;left:0;width:700px;height:22px;background:var(--dark);display:flex;justify-content:flex-end;align-items:center;padding-right:36px;gap:6px}
.topbar .phone{color:var(--silver);font-size:9px;margin-right:8px}
.social{width:13px;height:13px;border-radius:50%;border:1px solid var(--mid)}

/* header */
.header{position:absolute;top:22px;left:0;width:700px;height:66px;background:var(--white);display:flex;align-items:center;justify-content:space-between;padding:0 40px 0 90px}
.brand{display:flex;align-items:center;gap:8px}
.brand .mark{width:18px;height:18px;background:var(--ink)}
.brand .name{font-weight:700;font-size:18px;letter-spacing:0.5px;color:var(--ink)}
.nav{display:flex;gap:8px}
.nav a{font-size:10px;font-weight:500;color:var(--ink);text-decoration:none;padding:6px 12px;letter-spacing:0.4px}
.nav a.active{border:1px solid var(--ink)}

/* hero */
.hero{position:absolute;top:88px;left:0;width:700px;height:300px;background:linear-gradient(100deg,#8d9095 0%,#d9dadc 28%,#f2f2f1 45%,#c8c9cb 60%,#e7c04a 82%,#d7a52a 100%)}
.hero-caption{position:absolute;left:65px;top:146px;width:262px;background:rgba(30,30,32,0.78);padding:10px 12px}
.hero-caption h1{font-size:14px;font-weight:700;color:var(--white);line-height:1.25;letter-spacing:0.3px}
.hero-caption p{font-size:8.5px;color:var(--silver);margin-top:4px;letter-spacing:0.5px}
.hero-dot{position:absolute;left:338px;top:276px;width:24px;height:24px;border-radius:50%;background:var(--white)}

/* about */
.about{position:absolute;top:388px;left:0;width:700px;height:182px;text-align:center}
.section-title{font-size:19px;font-weight:700;letter-spacing:0.5px;color:var(--ink)}
.section-title span{font-weight:300}
.about .section-title{margin-top:22px}
.tabs{display:flex;justify-content:center;gap:6px;margin-top:10px}
.tabs span{font-size:8.5px;font-weight:500;padding:5px 10px;color:var(--mid)}
.tabs span.active{border:1px solid var(--ink);color:var(--ink)}
.about p{width:560px;margin:12px auto 0;font-size:8.5px;line-height:1.55;color:var(--mid)}

/* portfolio */
.portfolio{position:absolute;top:570px;left:0;width:700px;height:420px;background:var(--light);text-align:center}
.portfolio .section-title{margin-top:18px}
.filters{display:flex;justify-content:center;gap:14px;margin-top:14px;align-items:center}
.filters span{font-size:8.5px;color:var(--mid);padding:3px 7px}
.filters span.active{border:1px solid var(--ink);color:var(--ink);font-weight:700}
.gallery{position:absolute;top:0;left:0}
.slider{position:absolute;top:376px;left:0;width:700px;display:flex;justify-content:center;align-items:center;gap:6px}
.slider .arrow{font-size:12px;color:var(--mid);margin:0 4px}
.slider .dot{width:6px;height:6px;border-radius:50%;background:var(--silver)}
.slider .dot.on{background:var(--ink)}

/* footer */
.footer{position:absolute;top:990px;left:0;width:700px;height:182px;background:var(--dark);color:var(--silver)}
.col{position:absolute;top:22px}
.col h4{font-size:9.5px;font-weight:700;color:var(--white);letter-spacing:0.4px;margin-bottom:12px}
.col ul{list-style:none}
.col li{font-size:8px;margin-bottom:9px;padding-left:8px;position:relative}
.col li::before{content:"";position:absolute;left:0;top:3px;width:3px;height:3px;background:var(--silver)}
.contact-line{display:flex;gap:6px;font-size:8px;line-height:1.4;margin-bottom:9px}
.contact-line .ico{flex:none;width:10px;height:10px}
.field{width:140px;height:17px;border:1px solid #4a4b4f;background:#2b2c2f;font-size:7.5px;color:var(--mid);padding:3px 5px;margin-bottom:6px}
.field.tall{height:26px}
.submit{display:inline-block;background:var(--white);color:var(--ink);font-size:7.5px;font-weight:700;padding:4px 10px}
.bottombar{position:absolute;top:1172px;left:0;width:700px;height:28px;background:var(--darker);display:flex;align-items:center;justify-content:space-between;padding:0 55px}
.bottombar p{font-size:8px;color:var(--mid)}
.bottombar .icons{display:flex;gap:6px}
</style>
</head>
<body>
<div class="page">

  <div class="topbar">
    <span class="phone">+61 7 3000 0000</span>
    <span class="social"></span><span class="social"></span><span class="social"></span><span class="social"></span>
  </div>

  <header class="header">
    <div class="brand"><span class="mark"></span><span class="name">HARBOURLINE</span></div>
    <nav class="nav">
      <a class="active" href="#">HOME</a>
      <a href="#">ABOUT US</a>
      <a href="#">PORTFOLIO</a>
      <a href="#">CONTACT US</a>
    </nav>
  </header>

  <section class="hero" role="img" aria-label="Modern office interior with glass partitions and coloured glazing">
    <div class="hero-caption">
      <h1>WE SPECIALISE IN COMMERCIAL<br>OFFICE FIT OUTS</h1>
      <p>PARTITIONS, GLASS, DOORS ETC</p>
    </div>
    <span class="hero-dot"></span>
  </section>

  <section class="about">
    <h2 class="section-title">ABOUT HARBOURLINE <span>FITOUTS</span></h2>
    <div class="tabs"><span class="active">ABOUT US</span><span>WHAT WE OFFER</span></div>
    <p>Harbourline Fitouts delivers commercial office fitouts across Queensland, from glass partitions and doors to complete workplace builds. Our team plans, builds and finishes every project on time, with clean detailing and durable materials. We work closely with owners, tenants and designers to create offices that look sharp and work well for the people inside them every day.</p>
  </section>

  <section class="portfolio">
    <h2 class="section-title">PORTFOLIO</h2>
    <div class="filters">
      <span>&lsaquo;</span><span>ALL</span><span class="active">2016</span><span>2015</span><span>2014</span><span>2013</span><span>2012</span><span>&rsaquo;</span>
    </div>
    <svg class="gallery" width="700" height="420" viewBox="0 0 700 420">
      <defs>
        <linearGradient id="g1" x1="0" y1="0" x2="1" y2="1"><stop offset="0" stop-color="#d8d9db"/><stop offset="1" stop-color="#6d7076"/></linearGradient>
        <linearGradient id="g2" x1="0" y1="0" x2="1" y2="1"><stop offset="0" stop-color="#5a5c60"/><stop offset="1" stop-color="#c7c8ca"/></linearGradient>
        <linearGradient id="g3" x1="0" y1="0" x2="1" y2="1"><stop offset="0" stop-color="#c9a77d"/><stop offset="1" stop-color="#5b4733"/></linearGradient>
        <linearGradient id="g4" x1="0" y1="0" x2="0" y2="1"><stop offset="0" stop-color="#e3e4e6"/><stop offset="1" stop-color="#8e9196"/></linearGradient>
      </defs>
      <g transform="translate(0,70)">
        <polygon role="img" aria-label="Open office fitout with workstations" fill="url(#g1)" points="117.5,0 187.5,40 187.5,120 117.5,160 47.5,120 47.5,40"/>
        <polygon role="img" aria-label="Meeting room behind glass partition" fill="url(#g2)" points="272.5,0 342.5,40 342.5,120 272.5,160 202.5,120 202.5,40"/>
        <polygon role="img" aria-label="Office reception with timber finishes" fill="url(#g3)" points="427.5,0 497.5,40 497.5,120 427.5,160 357.5,120 357.5,40"/>
        <polygon fill="rgba(20,20,22,0.45)" points="427.5,0 497.5,40 497.5,120 427.5,160 357.5,120 357.5,40"/>
        <text x="427.5" y="82" text-anchor="middle" fill="#fff" font-family="Roboto, Arial, sans-serif" font-size="9" font-weight="700">LOREM IPSUM DOLOR</text>
        <text x="427.5" y="95" text-anchor="middle" fill="#ddd" font-family="Roboto, Arial, sans-serif" font-size="7">Office fitout</text>
        <polygon role="img" aria-label="Boardroom with glass walls" fill="url(#g2)" points="582.5,0 652.5,40 652.5,120 582.5,160 512.5,120 512.5,40"/>
        <polygon role="img" aria-label="Frosted glass partition detail" fill="url(#g4)" points="195,133 265,173 265,253 195,293 125,253 125,173"/>
        <polygon role="img" aria-label="Office corridor with glazed doors" fill="url(#g1)" points="350,133 420,173 420,253 350,293 280,253 280,173"/>
        <polygon role="img" aria-label="Glass office door" fill="url(#g2)" points="505,133 575,173 575,253 505,293 435,253 435,173"/>
      </g>
    </svg>
    <div class="slider">
      <span class="arrow">&lsaquo;</span><span class="dot"></span><span class="dot on"></span><span class="dot"></span><span class="dot"></span><span class="arrow">&rsaquo;</span>
    </div>
  </section>

  <footer class="footer">
    <div class="col" style="left:55px">
      <h4>QUICK LINK</h4>
      <ul><li>Home</li><li>About</li><li>Portfolio</li><li>Contact Us</li></ul>
    </div>
    <div class="col" style="left:175px;width:150px">
      <h4>CONTACT DETAILS</h4>
      <div class="contact-line"><svg class="ico" viewBox="0 0 10 10"><path d="M5 0.5a3 3 0 0 1 3 3c0 2.2-3 6-3 6s-3-3.8-3-6a3 3 0 0 1 3-3z" fill="#b9bcc1"/><circle cx="5" cy="3.5" r="1.1" fill="#222326"/></svg><span>12 Harbour Street,<br>Brisbane QLD 4000</span></div>
      <div class="contact-line"><svg class="ico" viewBox="0 0 10 10"><path d="M2 0.8l1.8 1.9-1 1.2a6 6 0 0 0 3.3 3.3l1.2-1 1.9 1.8-1.2 1.5C5 9.2 0.8 5 0.5 2z" fill="#b9bcc1"/></svg><span>07 3000 0000</span></div>
      <div class="contact-line"><svg class="ico" viewBox="0 0 10 10"><rect x="0.5" y="2" width="9" height="6" fill="none" stroke="#b9bcc1"/><path d="M0.5 2l4.5 3.5L9.5 2" fill="none" stroke="#b9bcc1"/></svg><span>info@harbourline.example</span></div>
    </div>
    <div class="col" style="left:350px">
      <h4>LOCATION MAP</h4>
      <svg width="90" height="100" viewBox="0 0 90 100"><polygon role="img" aria-label="Street map showing office location" fill="#c9d3bf" points="45,0 88,25 88,75 45,100 2,75 2,25"/></svg>
    </div>
    <div class="col" style="left:500px">
      <h4>GET A FREE QUOTE</h4>
      <div class="field">Your Name</div>
      <div class="field">Your Email</div>
      <div class="field tall">Your Message</div>
      <span class="submit">SUBMIT</span>
    </div>
  </footer>

  <div class="bottombar">
    <p>&copy; 2016. HARBOURLINE. All Rights Reserved</p>
    <div class="icons"><span class="social"></span><span class="social"></span><span class="social"></span><span class="social"></span></div>
  </div>

</div>
</body>
</html>
```